Empower our Electric Journey on the Web

We need a new website that can promote our services. Our three services that we offer are:
- Management of e-mobility charging stations
- Management of energy purchases
- Leasing of E-Mobility charging stations
- Energy billing of private electricity meters
The website should work responsively on PC, tablet and smartphone. In general, a simple navigation and an appealing design should be in the foreground. The website should give the customer the possibility to request , based pm a preset chexkbox chart and to get in contact with us.
Our logo works on black and white background.
Our slogan is:
Empower Your Electric Journey with Velnik Mobility
The 4 Pages should be the following:
Main Page, with info about us, why choose us,
2nd; services; what we sell and what are our services
3rd; Contact us, request an offer
4th, References about costumers and Work we already did, in the future we would like to integrate a Blog Post in this section in stead of references.

Target Market(s)

Landlords, Homeowners, Homeowner Associations

Industry/Entity Type

EV Chargers / E-Mobility

Coding

Coded - Design and coding required

Number of Pages Required

4 page

Requirements
Nice to have
• Pop up to our mailchimp newsletter subscription

```html
<!DOCTYPE html>
<html lang="en">
<head>
<meta charset="utf-8">
<title>Velnik Mobility</title>
<link rel="stylesheet" href="https://fonts.googleapis.com/css2?family=Poppins:wght@400;500;600;700&family=Noto+Serif:wght@700&display=swap">
<style>
:root{
  --green:#3cb83a;
  --green-dark:#2a9c2b;
  --green-soft:#eef8ea;
  --ink:#1b1b1b;
  --muted:#555;
  --grey:#dcdcdc;
  --black:#0d0d0d;
  --white:#fff;
}
*{box-sizing:border-box;margin:0;padding:0}
html,body{width:1200px;height:5046px;overflow:hidden}
body{position:relative;font-family:"Poppins",sans-serif;color:var(--ink);background:var(--white)}
.abs{position:absolute}
.brand{display:flex;align-items:center;gap:10px;font-weight:700;color:var(--green);font-size:22px;letter-spacing:1px;text-transform:uppercase}
.brand .mark{width:18px;height:18px;background:var(--green)}
/* header */
.site-header{top:0;left:0;width:1200px;height:68px;background:var(--white);z-index:5}
.site-header .brand{position:absolute;left:114px;top:20px}
.main-nav{position:absolute;left:423px;top:25px;display:flex;gap:30px;font-size:13px;font-weight:500;text-transform:uppercase}
.header-cta{position:absolute;right:0;top:0;width:242px;height:68px;background:var(--green);color:var(--white);display:flex;align-items:center;justify-content:center;gap:10px;font-size:15px;font-weight:500;text-transform:uppercase}
/* buttons */
.btn{position:absolute;display:flex;align-items:center;justify-content:center;gap:8px;height:43px;border-radius:22px;font-size:12px;font-weight:600;text-transform:uppercase}
.btn-outline{border:2px solid var(--green);color:var(--green);background:transparent}
.btn-solid{background:var(--green);color:var(--white)}
/* section titles */
.eyebrow{font-size:12px;font-weight:600;color:var(--green-dark);text-transform:uppercase}
.title{font-size:34px;font-weight:600;text-transform:uppercase;line-height:1.1}
.rule{width:84px;height:3px;background:var(--green)}
.centered{left:0;width:1200px;text-align:center}
.centered .rule{margin:14px auto 0}
/* hero */
.hero{top:68px;left:0;width:1200px;height:600px;background:linear-gradient(90deg,#d3d3d3,#e6e6e6 55%,#cfd3cf)}
.hero-photo{left:470px;top:68px;width:730px;height:580px;background:linear-gradient(120deg,#e9ecea 0%,#b9c3b8 45%,#5d6b5a 80%,#2e3530 100%)}
.hero-title{left:150px;top:200px;font-size:37px;font-weight:600;line-height:1.32;text-transform:uppercase}
.slide-arrow{width:42px;height:42px;border-radius:50%;background:rgba(255,255,255,.85);display:flex;align-items:center;justify-content:center}
/* about */
.about-text{left:149px;top:760px;width:470px}
.about-text p{font-size:14.5px;line-height:26px;margin-top:0}
.about-photo{left:643px;top:697px;width:557px;height:473px;background:linear-gradient(160deg,#1e2a2a,#4d5b3a 50%,#8a7a4a 70%,#2f3a26);border-radius:260px 40px 60px 240px / 200px 60px 240px 260px}
/* services */
.service{width:234px;height:234px;border-radius:50%;background:radial-gradient(circle at 50% 40%,#5ccf4f,#36b030);color:var(--white);display:flex;align-items:center;justify-content:center;text-align:center;font-size:13px;line-height:24px;padding:0 24px;box-shadow:0 10px 30px rgba(60,184,58,.25)}
/* why */
.why-photo{left:0;top:2226px;width:564px;height:437px;background:linear-gradient(110deg,#334141,#6b7c80 40%,#a58d66 70%,#d9c8a0);border-radius:0 120px 180px 0 / 0 300px 140px 0}
.why-text{left:611px;top:2276px;width:450px;font-size:14.5px;line-height:26px}
.checks{list-style:none;margin-top:14px}
.checks li{display:flex;align-items:center;gap:10px;font-size:14.5px;height:35px}
.checks i{width:14px;height:14px;border-radius:50%;background:#b7e2b1;display:inline-block}
/* blog */
.blog-feature{left:184px;top:2976px;width:409px;height:231px;background:linear-gradient(100deg,#1f2b2c,#5a6660 50%,#9aa39d)}
.thumb{left:625px;width:123px;height:114px}
.meta{font-size:12.5px;color:var(--muted)}
.post-title{font-family:"Noto Serif",serif;font-weight:700;font-size:15.5px;line-height:22px;color:var(--ink)}
.read{font-size:14px;font-weight:600;color:var(--green-dark);text-transform:uppercase;display:flex;align-items:center;gap:8px}
.divider{left:625px;width:395px;height:1px;background:#cfe3cb}
/* partners */
.partner{top:3812px;width:206px;height:108px;background:var(--white);box-shadow:0 4px 18px rgba(0,0,0,.08);display:flex;align-items:center;justify-content:center}
.partner .brand{font-size:18px}
.partner .brand .mark{width:14px;height:14px}
/* contact */
.contact-form{left:276px;top:4392px;width:648px;height:301px;background:var(--green);border-radius:0 90px 0 90px}
.field{position:absolute;color:var(--white);font-size:11.5px}
.field span{display:block;height:24px;border-bottom:1px solid rgba(255,255,255,.7)}
.submit{left:537px;top:4636px;width:131px;height:32px;background:var(--black);color:var(--white);border-radius:16px;font-size:9px;font-weight:600;display:flex;align-items:center;justify-content:center;text-transform:uppercase}
/* footer */
.site-footer{top:4840px;left:0;width:1200px;height:206px;background:var(--black);color:var(--white)}
.footer-badge{left:567px;top:4788px;width:72px;height:72px;border-radius:50%;background:var(--white);display:flex;align-items:center;justify-content:center}
.footer-nav{top:4902px;left:0;width:1200px;display:flex;justify-content:center;gap:32px;font-size:12px;font-weight:500;text-transform:uppercase;color:var(--white)}
.copy{top:4935px;left:0;width:1200px;text-align:center;font-size:11px;color:var(--white)}
.social{left:585px;top:4965px;width:36px;height:36px;border-radius:50%;border:2px solid var(--white)}
</style>
</head>
<body>

<header class="abs site-header">
  <div class="brand"><span class="mark"></span>Velnik Mobility</div>
  <nav class="main-nav"><span>Home</span><span>About Us</span><span>Why Choose Us</span><span>Our Services</span><span>Blogs</span></nav>
  <div class="header-cta">
    <svg width="18" height="18" viewBox="0 0 24 24" fill="none" stroke="#fff" stroke-width="2"><path d="M5 3h4l2 5-3 2a12 12 0 0 0 6 6l2-3 5 2v4a2 2 0 0 1-2 2A17 17 0 0 1 3 5a2 2 0 0 1 2-2z"/></svg>
    Contact Us
  </div>
</header>

<section>
  <div class="abs hero"></div>
  <div class="abs hero-photo" role="img" aria-label="Woman with a phone leaning on an electric car at a roadside charging post"></div>
  <svg class="abs" style="left:0;top:480px" width="1200" height="200" viewBox="0 0 1200 200" aria-hidden="true">
    <path d="M0 150 C120 80 240 160 360 165 C520 170 620 60 760 80 C900 100 960 150 1080 140 C1150 132 1180 110 1200 100 L1200 200 L0 200Z" fill="#fff"/>
  </svg>
  <h1 class="abs hero-title">Empower Your<br>Electric Journey with<br>Velnik Mobility</h1>
  <a class="btn btn-outline" style="left:147px;top:376px;width:174px;height:40px">Contact Us
    <svg width="16" height="10" viewBox="0 0 16 10" fill="none" stroke="currentColor" stroke-width="1.5"><path d="M0 5h14M10 1l4 4-4 4"/></svg></a>
  <div class="abs slide-arrow" style="left:33px;top:255px"><svg width="12" height="14" viewBox="0 0 12 14" fill="none" stroke="#222" stroke-width="2"><path d="M8 1 2 7l6 6"/></svg></div>
  <div class="abs slide-arrow" style="left:1101px;top:255px"><svg width="12" height="14" viewBox="0 0 12 14" fill="none" stroke="#222" stroke-width="2"><path d="m4 1 6 6-6 6"/></svg></div>
</section>

<section>
  <div class="abs about-text">
    <div class="eyebrow">Who We Are</div>
    <h2 class="title" style="margin-top:10px">About Us</h2>
    <div class="rule" style="margin:10px 0 14px"></div>
    <p><strong style="font-weight:600">Lorem Ipsum has been the industry's standard dummy text ever since the 1500s, when an unknown.</strong><br>printer took a galley of type and scrambled it to make a type specimen book. It has survived not only five centuries, but also the leap into electronic typesetting, remaining essentially unchanged. It was popularised in the 1960s with the release of Letraset sheets containing Lorem Ipsum passages, and more recently with desktop publishing</p>
  </div>
  <a class="btn btn-solid" style="left:147px;top:1075px;width:176px">Learn More
    <svg width="16" height="10" viewBox="0 0 16 10" fill="none" stroke="currentColor" stroke-width="1.5"><path d="M0 5h14M10 1l4 4-4 4"/></svg></a>
  <div class="abs about-photo" role="img" aria-label="Row of illuminated charging stations along a path at dusk"></div>
</section>

<section>
  <svg class="abs" style="left:0;top:1255px" width="1200" height="720" viewBox="0 0 1200 720" aria-hidden="true">
    <path d="M0 0H1200V710 C1120 640 1060 560 960 580 C820 610 760 700 620 690 C480 680 440 560 300 570 C180 580 90 660 0 640Z" fill="var(--green-soft)"/>
  </svg>
  <div class="abs centered" style="top:1322px">
    <div class="eyebrow">What We Offer</div>
    <h2 class="title" style="margin-top:8px">Our Services</h2>
    <div class="rule"></div>
  </div>
  <svg class="abs" style="left:150px;top:1430px" width="900" height="310" viewBox="0 0 900 310" fill="none" stroke="var(--green)" stroke-width="2" aria-hidden="true">
    <path d="M29 220 A143 143 0 0 1 300 120"/>
    <path d="M305 140 A143 143 0 0 0 580 220"/>
    <path d="M600 200 A143 143 0 0 1 870 120"/>
    <circle cx="29" cy="220" r="5" fill="var(--green)" stroke="none"/>
    <path d="M296 118 l4 6 l4 -6" />
    <path d="M580 212 l6 8 -10 2" />
    <circle cx="870" cy="130" r="5" fill="var(--green)" stroke="none"/>
  </svg>
  <div class="abs service" style="left:187px;top:1463px" role="img" aria-label="Charging station service photo tinted green">Management of e-mobility charging stations</div>
  <div class="abs service" style="left:475px;top:1463px" role="img" aria-label="Consultants beside an electric car tinted green">Management of energy purchases</div>
  <div class="abs service" style="left:766px;top:1463px" role="img" aria-label="Charging plug close-up tinted green">Energy billing of private electricity meters</div>
  <a class="btn btn-outline" style="left:508px;top:1769px;width:176px">Learn More
    <svg width="16" height="10" viewBox="0 0 16 10" fill="none" stroke="currentColor" stroke-width="1.5"><path d="M0 5h14M10 1l4 4-4 4"/></svg></a>
</section>

<section>
  <div class="abs centered" style="top:2046px">
    <div class="eyebrow" style="font-size:11px">Why Choose Us</div>
    <h2 class="title" style="margin-top:8px">Why Choose Us</h2>
    <div class="rule"></div>
    <p style="font-size:14.5px;line-height:27px;margin-top:18px">Lorem Ipsum has been the industry's standard dummy text ever since the 1500s.<br>when an unknown printer took a galley.</p>
  </div>
  <div class="abs why-photo" role="img" aria-label="Electric cars plugged in along a row of street chargers"></div>
  <div class="abs why-text">
    <p>Lorem Ipsum has been the industry's standard dummy text ever since the 1500s, when an unknown.<br>printer took a galley of type and scrambled it to make a type specimen book. It has survived</p>
    <ul class="checks">
      <li><i></i>Energy billing of private electricity meters</li>
      <li><i></i>Management of energy purchases</li>
      <li><i></i>Leasing of E-Mobility charging stations</li>
      <li><i></i>Management of e-mobility charging stations</li>
    </ul>
  </div>
  <a class="btn btn-solid" style="left:607px;top:2551px;width:176px">Learn More
    <svg width="16" height="10" viewBox="0 0 16 10" fill="none" stroke="currentColor" stroke-width="1.5"><path d="M0 5h14M10 1l4 4-4 4"/></svg></a>
</section>

<section>
  <svg class="abs" style="left:0;top:2720px" width="1200" height="850" viewBox="0 0 1200 850" aria-hidden="true">
    <path d="M0 20 C90 40 120 120 240 110 C360 100 400 20 520 30 C660 45 700 120 820 100 C960 80 1060 40 1200 70 V810 C1100 760 1000 700 860 730 C720 760 640 830 500 820 C360 810 300 740 180 750 C100 760 50 800 0 820Z" fill="var(--green-soft)"/>
  </svg>
  <div class="abs centered" style="top:2872px">
    <div class="eyebrow" style="color:var(--ink);font-weight:500;font-size:11px">Blogs</div>
    <h2 class="title" style="margin-top:8px">Latest Blogs</h2>
    <div class="rule"></div>
  </div>
  <div class="abs blog-feature" role="img" aria-label="Charging cable plugged into a car beside a charging post"></div>
  <div class="abs" style="left:187px;top:3230px;width:400px">
    <div class="meta">April 12, 2023 &nbsp;|&nbsp; No Comments</div>
    <div class="post-title" style="margin-top:6px">Mauris vel lacus vitae felis vestibulum volutpat Etiam est nunc venenatitristique</div>
    <p style="font-size:11px;line-height:20px;color:#666;margin-top:8px">Nunc tempus felis vitae urna Vivamus porttitor neque at volutpat rutrum purus nisi eleifend libero a tempus libero lectus</p>
    <div class="read" style="margin-top:10px">Learn More <svg width="14" height="10" viewBox="0 0 16 10" fill="none" stroke="currentColor" stroke-width="1.5"><path d="M0 5h14M10 1l4 4-4 4"/></svg></div>
  </div>

  <div class="abs thumb" style="top:2976px;background:linear-gradient(120deg,#c9d3d8,#7a8790)" role="img" aria-label="Hand holding a charging plug"></div>
  <div class="abs" style="left:773px;top:2982px;width:250px">
    <div class="meta">April 08, 2023 &nbsp;|&nbsp; No Comments</div>
    <div class="post-title" style="margin-top:6px">Mauris vel lacus vitae felis vestibulum volutpat</div>
    <div class="read" style="margin-top:8px">Learn More <svg width="14" height="10" viewBox="0 0 16 10" fill="none" stroke="currentColor" stroke-width="1.5"><path d="M0 5h14M10 1l4 4-4 4"/></svg></div>
  </div>
  <div class="abs divider" style="top:3104px"></div>

  <div class="abs thumb" style="top:3127px;background:linear-gradient(120deg,#dfe2e4,#8d959a)" role="img" aria-label="Wall charger beside a parked car"></div>
  <div class="abs" style="left:773px;top:3125px;width:250px">
    <div class="meta">April 06, 2023 &nbsp;|&nbsp; No Comments</div>
    <div class="post-title" style="margin-top:6px">Fusce tellus Sed metus augue convallis et</div>
    <div class="read" style="margin-top:8px">Learn More <svg width="14" height="10" viewBox="0 0 16 10" fill="none" stroke="currentColor" stroke-width="1.5"><path d="M0 5h14M10 1l4 4-4 4"/></svg></div>
  </div>
  <div class="abs divider" style="top:3262px"></div>

  <div class="abs thumb" style="top:3282px;background:linear-gradient(120deg,#4d4a44,#a08d72)" role="img" aria-label="Woman charging her car"></div>
  <div class="abs" style="left:777px;top:3283px;width:250px">
    <div class="meta">April 02, 2023 &nbsp;|&nbsp; No Comments</div>
    <div class="post-title" style="margin-top:6px">Phasellus felis dolor scelerisque a tempus</div>
    <div class="read" style="margin-top:8px">Learn More <svg width="14" height="10" viewBox="0 0 16 10" fill="none" stroke="currentColor" stroke-width="1.5"><path d="M0 5h14M10 1l4 4-4 4"/></svg></div>
  </div>
</section>

<section>
  <div class="abs centered" style="top:3683px">
    <div class="eyebrow" style="font-size:11px">Partners</div>
    <h2 class="title" style="margin-top:8px">Our Partners</h2>
    <div class="rule"></div>
  </div>
  <div class="abs partner" style="left:141px"><div class="brand"><span class="mark"></span>Velnik Mobility</div></div>
  <div class="abs partner" style="left:374px"><div class="brand"><span class="mark"></span>Velnik Mobility</div></div>
  <div class="abs partner" style="left:607px"><div class="brand"><span class="mark"></span>Velnik Mobility</div></div>
  <div class="abs partner" style="left:838px"><div class="brand"><span class="mark"></span>Velnik Mobility</div></div>
  <a class="btn btn-outline" style="left:517px;top:3953px;width:176px">View More
    <svg width="16" height="10" viewBox="0 0 16 10" fill="none" stroke="currentColor" stroke-width="1.5"><path d="M0 5h14M10 1l4 4-4 4"/></svg></a>
</section>

<section>
  <svg class="abs" style="left:0;top:4140px" width="1200" height="700" viewBox="0 0 1200 700" aria-hidden="true">
    <path d="M0 40 C120 20 200 110 340 110 C500 110 560 10 720 20 C880 30 960 110 1080 90 C1140 80 1180 50 1200 40 V700 H0Z" fill="var(--green-soft)"/>
  </svg>
  <div class="abs centered" style="top:4292px">
    <div class="eyebrow" style="font-size:11px">Get In Touch</div>
    <h2 class="title" style="margin-top:8px">Leave Us A Message</h2>
    <div class="rule"></div>
  </div>
  <form class="abs contact-form">
    <label class="field" style="left:73px;top:52px;width:242px">First Name<span></span></label>
    <label class="field" style="left:337px;top:52px;width:241px">Email address<span></span></label>
    <label class="field" style="left:73px;top:105px;width:242px">Last Name<span></span></label>
    <label class="field" style="left:337px;top:105px;width:241px">Phone number<span></span></label>
    <label class="field" style="left:73px;top:150px;width:505px">Message<span style="height:52px"></span></label>
  </form>
  <div class="abs submit">Submit Message &rsaquo;</div>
</section>

<footer>
  <div class="abs site-footer"></div>
  <div class="abs footer-badge"><span style="width:22px;height:22px;background:var(--green);display:block"></span></div>
  <nav class="abs footer-nav"><span>Home</span><span>About Us</span><span>Why Choose Us</span><span>Our Services</span><span>Blogs</span><span>Contact Us</span></nav>
  <div class="abs copy">© 2023 Velnik Mobility | All Rights Reserved | Disclaimer</div>
  <div class="abs social" aria-label="Social profile"></div>
</footer>

</body>
</html>
```